Letterhead

We have a new logo and would like to design electronic letterhead with our new logo. We have two office locations. One of our offices is moving in July.

```html
<!DOCTYPE html>
<html lang="en">
<head>
<meta charset="utf-8">
<title>Halden Rowe Law – Letterhead</title>
<link href="https://fonts.googleapis.com/css2?family=Montserrat:wght@300;400;500;600&family=Allura&display=swap" rel="stylesheet">
<style>
  :root {
    --backdrop: #e9e9ea;
    --paper: #f6f6f6;
    --navy: #141a36;
    --blue: #1f67b8;
    --ink: #2b2b2b;
    --muted: #8a8a8a;
    --body: #7a7a7a;
  }
  * { margin: 0; padding: 0; box-sizing: border-box; }
  html, body { width: 1110px; height: 1200px; overflow: hidden; background: var(--backdrop); }
  body { font-family: "Montserrat", sans-serif; position: relative; }

  .letterhead {
    position: absolute; left: 174px; top: 50px;
    width: 772px; height: 1079px;
    background: var(--paper);
    box-shadow: 0 4px 18px rgba(0,0,0,0.12);
  }

  .brand-name {
    position: absolute; left: 0; right: 0; top: 62px;
    text-align: center;
    font-weight: 600; font-size: 30px; letter-spacing: 1px; line-height: 36px;
    color: var(--navy);
  }
  .band { position: absolute; background: var(--blue); height: 11px; top: 109px; }
  .band--left { left: 0; width: 273px; }
  .band--right { left: 495px; right: 0; }
  .rule-navy { position: absolute; left: 0; right: 0; top: 127px; height: 3px; background: var(--navy); }

  .recipient { position: absolute; left: 79px; top: 238px; }
  .recipient__label { font-size: 13px; letter-spacing: 2px; line-height: 18px; color: var(--ink); margin-bottom: 4px; }
  .recipient__name { font-size: 12px; line-height: 17px; color: var(--blue); margin-bottom: 3px; }
  .recipient__line { font-size: 9.5px; line-height: 17px; color: var(--muted); font-weight: 300; }

  .letter-date { position: absolute; right: 77px; top: 238px; font-size: 10.5px; line-height: 16px; color: var(--ink); }

  .letter-body {
    position: absolute; left: 79px; top: 384px; width: 616px;
    font-size: 10px; line-height: 13.5px; color: var(--body); text-align: justify;
  }
  .letter-body p { margin-bottom: 13.5px; }

  .signature { position: absolute; left: 79px; top: 758px; font-family: "Allura", cursive; font-size: 30px; line-height: 36px; color: var(--ink); }
  .signer__name { position: absolute; left: 79px; top: 802px; font-size: 12px; line-height: 16px; color: var(--ink); }
  .signer__role { position: absolute; left: 79px; top: 819px; font-size: 9px; line-height: 13px; color: var(--muted); font-weight: 300; }

  .footer-rule { position: absolute; top: 1034px; height: 1px; background: var(--navy); }
  .footer-rule--left { left: 0; width: 283px; }
  .footer-rule--right { left: 489px; right: 0; }
  .footer-address { position: absolute; left: 0; right: 0; top: 1026px; text-align: center; font-size: 12px; line-height: 16px; color: var(--ink); }

  .footer-contacts {
    position: absolute; left: 0; right: 0; top: 1047px;
    display: flex; justify-content: center; gap: 18px;
    font-size: 12px; line-height: 16px; color: var(--ink);
  }
  .contact { display: flex; align-items: center; gap: 7px; }
  .contact svg { width: 9px; height: 9px; fill: var(--blue); }
</style>
</head>
<body>
  <main class="letterhead">
    <header>
      <div class="brand-name">HALDEN ROWE LAW</div>
      <div class="band band--left"></div>
      <div class="band band--right"></div>
      <div class="rule-navy"></div>
    </header>

    <section class="recipient">
      <div class="recipient__label">TO</div>
      <div class="recipient__name">Daniel Ferro</div>
      <div class="recipient__line">Human Resources</div>
      <div class="recipient__line">Northwind Inc.</div>
      <div class="recipient__line">2210-B Larkspur Avenue, Ashford</div>
      <div class="recipient__line">E42 USA</div>
    </section>

    <div class="letter-date">Friday, 01/01/2018</div>

    <article class="letter-body">
      <p>Lorem ipsum dolor sit amet, consectetuer adipiscing elit, sed diam nonummy nibh euismod tincidunt ut laoreet dolore magna aliquam erat volutpat. Ut wisi enim ad minim veniam, quis nostrud exerci tationmcorper suscipit lobortis nisl ut aliquip ex ea commodo consequat. Duis autem vel eum iriure dolor in hendrerit in vulputate velit esse molestie consequat, vel illum dolore eu feugiat nulla facilisis at vero eros et accumsan et iusto odio dignissim qui blandit praesent luptatum zzril delenit augue duis dolore te feugait nulla facilisi.</p>
      <p>Nam liber tempor cum soluta nobis eleifend option congue nihil imprdiet doming id quod mazim placerat facer possim assum. Typi non habent claritatem insitam;</p>
      <p>Est usus legentis in iis qui facit eorum claritatem.</p>
      <p>Investigationes demonstraverunt lectores legere me lius quod ii legunt saepius. Claritas est etiam processus dynamicus, qui sequitur mutationem consuetudium lectorum. Mirum est notare quam littera gothica, quam nunc putamus parum claram, anteposuerit litterarum formas humanitatis per seacula quarta decima et quinta decima. Eodem modo typi, qui nunc nobis videntur parum clari, fiant sollemnes in futurum.</p>
      <p>consectetuer adipiscing elit, sed diam nonummy nibh euismod tincidunt ut laoreet dolore magna aliquam erat volutpat. Ut wisi enim ad minim veniam, quis nostrud exerci tation ullamcorper suscipit lobortis nisl ut aliquip ex ea commodo consequat. Duis autem vel eum iriure dolor in hendrerit in vulputate velit esse molestie consequat, vel illum dolore eu feugiat nulla facilisis at vero eros et accumsan et iusto odio dignissim qui blandit praesent luptatum zzril delenit augue duis dolore te feugait nulla facilisi.</p>
      <p>Nam liber tempor cum soluta nobis eleifend option congue nihil imperdiet .</p>
    </article>

    <div class="signature">peter lindqvist</div>
    <div class="signer__name">Peter Lindqvist</div>
    <div class="signer__role">Managing Director</div>

    <footer>
      <div class="footer-rule footer-rule--left"></div>
      <div class="footer-address">Your address, city, state, ZIP 0000</div>
      <div class="footer-rule footer-rule--right"></div>
      <div class="footer-contacts">
        <span class="contact">
          <svg viewBox="0 0 10 10" aria-hidden="true"><path d="M2 0.5 L3.6 0.5 L4.2 3 L3 3.8 Q4 6 6.2 7 L7 5.8 L9.5 6.4 L9.5 8 Q9.5 9.5 8 9.5 Q0.5 9 0.5 2 Q0.5 0.5 2 0.5Z"/></svg>
          555-014-3870
        </span>
        <span class="contact">
          <svg viewBox="0 0 10 10" aria-hidden="true"><path d="M0.5 2 L9.5 2 L9.5 8.5 L0.5 8.5Z M0.5 2 L5 5.6 L9.5 2" stroke="#f6f6f6" stroke-width="0.8"/></svg>
          office@haldenrowe.com
        </span>
        <span class="contact">
          <svg viewBox="0 0 10 10" aria-hidden="true"><circle cx="5" cy="5" r="4.6"/><path d="M0.6 5 H9.4 M5 0.5 Q2.5 5 5 9.5 M5 0.5 Q7.5 5 5 9.5" stroke="#f6f6f6" stroke-width="0.7" fill="none"/></svg>
          www.haldenrowe.com
        </span>
      </div>
    </footer>
  </main>
</body>
</html>
```